Portal Panel Medic need professional looking business card printed on plastic, Commericial, Industri

We are family owned and operated garage door company in Indianapolis, Indiana. We sale service and install dock equipment, doors, operators. We are looking to expand our commercial/ industrial division. We also service all residential doors and operators. We are looking for a business that stands out of the crowd. We are committed to have the best customer service in the industry.

Target Market(s)

National and local general contractors, National/ Corpate service accounts,

Industry/Entity Type

Business Service

Contact Information for Business Card

To be printed on plastic stock

Font styles to use
Sans Serif

Colors
ffffff
f04a50
ec1f27

Requirements
Must have
• Name, website,email, phone number, position.
Nice to have
• A standout professional design

```html
<!DOCTYPE html>
<html lang="en">
<head>
<meta charset="utf-8">
<title>Portal Panel Medic — Business Card</title>
<link href="https://fonts.googleapis.com/css2?family=Open+Sans:wght@400;600&display=swap" rel="stylesheet">
<style>
  :root {
    --page-bg: #d9d3cb;
    --frost-light: #f4f2f0;
    --frost-mid: #e3ddd8;
    --brand-red: #ec1f27;
    --red-deep: #b3121a;
    --red-bright: #d9161f;
    --divider: #1a1a1a;
    --ink-warm: #e6c3a0;
  }
  * { box-sizing: border-box; margin: 0; padding: 0; }
  html, body { width: 1200px; height: 970px; overflow: hidden; }
  body {
    background: var(--page-bg);
    font-family: "Open Sans", sans-serif;
    position: relative;
  }
  .card {
    position: absolute;
    left: 178px; top: 272px;
    width: 845px; height: 474px;
    display: flex;
    box-shadow: 0 10px 28px rgba(0,0,0,.22);
  }
  .card__brand {
    width: 418px; height: 100%;
    background: linear-gradient(170deg, var(--frost-light) 0%, #eef1f5 40%, var(--frost-mid) 75%, #e8dbd8 100%);
    display: flex; align-items: center; justify-content: center;
  }
  .brand-name {
    color: var(--brand-red);
    font-weight: 600;
    font-size: 30px;
    line-height: 1.2;
    margin-top: -30px;
  }
  .card__divider { width: 6px; height: 100%; background: var(--divider); }
  .card__details {
    flex: 1; height: 100%;
    background: radial-gradient(ellipse at 70% 30%, var(--red-bright) 0%, var(--red-deep) 70%, #9c0f15 100%);
    color: var(--ink-warm);
    padding: 126px 0 0 82px;
  }
  .person-name { font-weight: 600; font-size: 26px; line-height: 34px; }
  .person-role { font-size: 19px; line-height: 26px; }
  .address { font-size: 19.5px; line-height: 28px; margin-top: 24px; }
  .contacts { list-style: none; margin-top: 19px; }
  .contacts li { display: flex; align-items: center; font-size: 19.5px; line-height: 28.5px; }
  .contacts svg { width: 16px; height: 16px; margin-right: 16px; flex: none; }
</style>
</head>
<body>
  <div class="card">
    <section class="card__brand">
      <h1 class="brand-name">Portal Panel Medic</h1>
    </section>
    <div class="card__divider"></div>
    <section class="card__details">
      <p class="person-name">John Smith</p>
      <p class="person-role">Manager</p>
      <p class="address">99th Street, Exact Road<br>New cross side, CA 456982.</p>
      <ul class="contacts">
        <li>
          <svg viewBox="0 0 20 20" aria-hidden="true"><path d="M4 2l3 0 1.5 4-2 1.5a10 10 0 0 0 6 6L14 11.5l4 1.5v3a2 2 0 0 1-2 2A14 14 0 0 1 2 4a2 2 0 0 1 2-2z" fill="var(--ink-warm)"/></svg>
          +999 9999 9999
        </li>
        <li>
          <svg viewBox="0 0 20 20" aria-hidden="true"><rect x="2" y="5" width="16" height="11" rx="1" fill="var(--ink-warm)"/><path d="M2 6l8 6 8-6" fill="none" stroke="var(--red-deep)" stroke-width="1.5"/></svg>
          info@mywebsite.com
        </li>
        <li>
          <svg viewBox="0 0 20 20" aria-hidden="true"><g fill="none" stroke="var(--ink-warm)" stroke-width="1.6"><circle cx="10" cy="10" r="8"/><ellipse cx="10" cy="10" rx="3.5" ry="8"/><path d="M2 10h16M4 5.5h12M4 14.5h12"/></g></svg>
          www.mywebsite.com
        </li>
      </ul>
    </section>
  </div>
</body>
</html>
```